Simple, Professional and neat business card design for Vendralo Inc.

We're looking to re-vamp our business card design. We're a supplier of innovative feed ingredients for the North American animal agriculture industry. We are located in Lucknow, Ontario, Canada and our flagship product is a product that prevents milk fever in dairy cows when the calve, it is fed before calving and is very effective compared to other alternatives available on the market today.

Our company has Danish roots and we import all of our product from our Danish partner/manufacturer in Denmark. We like our design to embrace high professionalism while remaining neat and simple.

Target Market(s)

B2B, Feed Mills, Veterinary Clinics, Large integrators/producers,

Industry/Entity Type

Agribusiness

Contact Information for Business Card

We like the rounded corners because they make the card easy to sit in a wallet and not many use it so it makes the card stand out, just possibly something to take account for during the design.

As you can also see on the sliders below, looking for a that simple but proffesional scandinavian design.

Requirements
Nice to have
• Rounded corners
Should not have
• Too vibrant

```html
<!DOCTYPE html>
<html lang="en">
<head>
<meta charset="utf-8">
<title>Vendralo Inc. Business Card</title>
<link href="https://fonts.googleapis.com/css2?family=Lato:wght@300;400;700;900&display=swap" rel="stylesheet">
<style>
  :root {
    --backdrop: #4a4a4a;
    --card: #ffffff;
    --brand-blue: #1a5fb4;
    --label-blue: #1e6fc2;
    --web-blue: #3d4fb8;
    --rule-blue: #6f86c9;
    --ink-dark: #3a3a3a;
    --ink-mid: #6a6a6a;
    --social-1: #3b5b9a;
    --social-2: #3aa9e0;
    --social-3: #b8352c;
  }
  * { box-sizing: border-box; margin: 0; padding: 0; }
  html, body {
    width: 1200px; height: 1200px; overflow: hidden;
    background: var(--backdrop);
    font-family: "Lato", sans-serif;
  }
  .stage {
    position: relative; width: 1200px; height: 1200px;
  }
  .card {
    position: absolute; top: 200px;
    width: 460px; height: 800px;
    background: var(--card);
    border-radius: 36px;
    text-align: center;
  }
  .card--front { left: 100px; }
  .card--back { left: 640px; }

  /* front */
  .front-mark {
    position: absolute; left: 50%; top: 130px;
    width: 170px; height: 170px; margin-left: -85px;
    border-radius: 50%; background: var(--brand-blue);
  }
  .front-name {
    position: absolute; left: 0; right: 0; top: 340px;
    font-weight: 900; font-size: 54px; letter-spacing: -0.5px;
    color: var(--brand-blue);
  }
  .front-web {
    position: absolute; left: 0; right: 0; bottom: 110px;
    font-weight: 300; font-size: 32px; color: var(--web-blue);
  }

  /* back */
  .back-brand {
    position: absolute; left: 0; right: 0; top: 118px;
    display: flex; align-items: center; justify-content: center; gap: 18px;
  }
  .back-brand__dot {
    width: 62px; height: 62px; border-radius: 50%; background: var(--brand-blue);
  }
  .back-brand__name {
    font-weight: 900; font-size: 44px; letter-spacing: -0.5px; color: var(--brand-blue);
  }
  .person {
    position: absolute; left: 0; right: 0; top: 318px;
    font-weight: 900; font-size: 38px; color: var(--ink-dark);
  }
  .contact {
    position: absolute; left: 90px; right: 90px; top: 400px;
  }
  .contact__group { padding: 8px 0 10px; }
  .contact__group + .contact__group { border-top: 1.5px solid var(--rule-blue); }
  .contact__line { font-size: 22px; line-height: 30px; color: var(--ink-mid); white-space: nowrap; }
  .contact__label { color: var(--label-blue); }
  .address {
    position: absolute; left: 0; right: 0; top: 660px;
    font-size: 18px; line-height: 26px; color: var(--ink-dark);
  }
  .social {
    position: absolute; left: 52px; bottom: 56px;
    display: flex; gap: 14px;
  }
  .social__item { width: 24px; height: 24px; border-radius: 4px; }
  .social__item--a { background: var(--social-1); }
  .social__item--b { background: var(--social-2); }
  .social__item--c { background: var(--social-3); }
</style>
</head>
<body>
<main class="stage">
  <section class="card card--front" aria-label="Card front">
    <div class="front-mark"></div>
    <h1 class="front-name">VENDRALO INC.</h1>
    <p class="front-web">www.vendralo.com</p>
  </section>

  <section class="card card--back" aria-label="Card back">
    <div class="back-brand">
      <span class="back-brand__dot"></span>
      <span class="back-brand__name">VENDRALO INC.</span>
    </div>
    <h2 class="person">ANDERS HOLMVIK</h2>
    <div class="contact">
      <div class="contact__group">
        <p class="contact__line"><span class="contact__label">Mobile:</span> 555 . 204 . 0187</p>
        <p class="contact__line"><span class="contact__label">Office:</span> 555 . 410 . 6623</p>
      </div>
      <div class="contact__group">
        <p class="contact__line"><span class="contact__label">Toll Free:</span> 800 . 555 . 0142</p>
        <p class="contact__line"><span class="contact__label">Fax:</span> 555 . 410 . 6690</p>
      </div>
      <div class="contact__group">
        <p class="contact__line"><span class="contact__label">Email:</span> anders@vendralo.com</p>
        <p class="contact__line"><span class="contact__label">Web:</span> www.vendralo.com</p>
      </div>
    </div>
    <p class="address">Box 412, Millbrook, Ontario Canada<br>N0B 3K1</p>
    <div class="social">
      <span class="social__item social__item--a"></span>
      <span class="social__item social__item--b"></span>
      <span class="social__item social__item--c"></span>
    </div>
  </section>
</main>
</body>
</html>
```